Biz card, stationary for geriatric clinic
ValdoNorte Residence & Geriatric SPA
Biz card, stationary for geriatric clinic - Health
Creative Brief
Professional
Dra. Tereza Lopes Amaral
Diretora
Dois Irmaos - RS
tereza@valdonorte.example
www.valdonorte.example
We will need stationary i.e. letterhead, envelope, etc. For all business cards we need editable files to change for multiple employees.
Mailing address: Rua Oitenta e sete, 418. CEP 41270-000 | Bairro Jardim Dois Irmaos - RS

```html
<!DOCTYPE html>
<html lang="pt">
<head>
<meta charset="utf-8">
<title>ValdoNorte Residence &amp; Geriatric SPA — Stationery</title>
<link rel="stylesheet" href="https://fonts.googleapis.com/css2?family=Cormorant+Garamond:wght@600&family=Open+Sans:wght@400;600&display=swap">
<style>
  :root{
    --bg:#2b2b2b;
    --paper:#ffffff;
    --gold:#c98a1e;
    --gold-light:#f0c463;
    --bronze:#7a4a12;
    --leaf:#6a8f2a;
    --ink:#3a3a3a;
    --ink-soft:#7a7a7a;
    --brand:#8a5a16;
  }
  *{box-sizing:border-box;margin:0;padding:0}
  html,body{width:1200px;height:754px;overflow:hidden;background:var(--bg)}
  body{font-family:"Open Sans",Arial,sans-serif;color:var(--ink)}
  .canvas{position:relative;width:1200px;height:754px;background:var(--bg)}
  .piece{position:absolute;background:var(--paper);overflow:hidden;box-shadow:0 6px 18px rgba(0,0,0,.45)}
  .wave{position:absolute;left:0;width:100%;display:block}

  /* brand lockup */
  .brand{display:flex;align-items:center;gap:8px}
  .brand-dot{flex:none;border-radius:50%;background:var(--gold)}
  .brand-name{font-family:"Cormorant Garamond",Georgia,serif;font-weight:600;color:var(--brand);line-height:1.05}

  /* letterhead */
  .letterhead{left:40px;top:52px;width:460px;height:650px}
  .letterhead .brand{position:absolute;top:26px;left:0;right:0;justify-content:center}
  .letterhead .brand-dot{width:30px;height:30px}
  .letterhead .brand-name{font-size:15px}
  .sender{position:absolute;top:82px;right:34px;text-align:right;font-size:7.5px;line-height:1.55;color:var(--ink-soft)}
  .letter-body{position:absolute;top:150px;left:40px;right:40px;font-size:8.5px;line-height:1.7}
  .letter-body p{margin-bottom:10px}
  .letter-date{margin-bottom:16px;color:var(--ink-soft)}
  .signature{margin-top:26px}
  .signature strong{display:block;font-weight:600}
  .letterhead .wave{bottom:0;height:118px}
  .letter-footer{position:absolute;bottom:14px;left:0;right:0;text-align:center;font-size:7.5px;color:#fff;letter-spacing:.2px}

  /* envelope */
  .envelope{left:540px;top:130px;width:620px;height:300px}
  .envelope .brand{position:absolute;top:26px;left:30px}
  .envelope .brand-dot{width:40px;height:40px}
  .envelope .brand-name{font-size:17px}
  .envelope-address{position:absolute;top:78px;left:30px;font-size:8px;line-height:1.6;color:var(--ink-soft)}
  .envelope .wave{bottom:0;height:120px}
  .envelope-web{position:absolute;bottom:18px;right:30px;font-size:10px;color:#fff;font-weight:600;letter-spacing:.3px}

  /* business cards */
  .card{top:454px;width:300px;height:170px}
  .card-front{left:540px}
  .card-front .brand{position:absolute;top:26px;left:22px}
  .card-front .brand-dot{width:38px;height:38px}
  .card-front .brand-name{font-size:15px}
  .card-front .wave{bottom:0;height:80px}
  .card-web{position:absolute;bottom:12px;right:18px;font-size:8.5px;font-weight:600;color:#fff}

  .card-back{left:860px;background:linear-gradient(160deg,var(--gold-light),var(--gold) 45%,var(--bronze))}
  .card-back .wave{top:0;height:70px}
  .contact{position:absolute;right:18px;bottom:16px;text-align:right;color:#fff;font-size:7.5px;line-height:1.6}
  .contact-name{font-size:10.5px;font-weight:600}
  .contact-role{font-size:8px;margin-bottom:6px}
</style>
</head>
<body>
<main class="canvas">

  <!-- Letterhead -->
  <section class="piece letterhead" aria-label="Papel timbrado">
    <div class="brand">
      <span class="brand-dot"></span>
      <span class="brand-name">ValdoNorte Residence &amp; Geriatric SPA</span>
    </div>
    <div class="sender">
      Dra. Tereza Lopes Amaral<br>
      Diretora<br>
      tereza@valdonorte.example<br>
      Dois Irmaos - RS
    </div>
    <div class="letter-body">
      <p class="letter-date">Dois Irmaos, 12 de março</p>
      <p>Sr. Paulo Menezes<br>Rua das Flores, 12</p>
      <p>Prezado Senhor,</p>
      <p>Agradecemos o seu interesse em nossa residência. Oferecemos cuidado diário, atividades de bem-estar e acompanhamento médico em um ambiente tranquilo e acolhedor.</p>
      <p>Nossa equipe está à disposição para uma visita e para apresentar os planos de estadia disponíveis.</p>
      <p>Atenciosamente,</p>
      <p class="signature"><strong>Dra. Tereza Lopes Amaral</strong>Diretora</p>
    </div>
    <svg class="wave" viewBox="0 0 460 118" preserveAspectRatio="none" aria-hidden="true">
      <defs>
        <linearGradient id="goldLetter" x1="0" y1="0" x2="1" y2="1">
          <stop offset="0" stop-color="#f0c463"/>
          <stop offset=".5" stop-color="#c98a1e"/>
          <stop offset="1" stop-color="#7a4a12"/>
        </linearGradient>
      </defs>
      <path d="M0 30 C140 90 300 0 460 24" fill="none" stroke="#6a8f2a" stroke-width="2"/>
      <path d="M0 42 C140 102 300 12 460 36 L460 118 L0 118 Z" fill="url(#goldLetter)"/>
    </svg>
    <p class="letter-footer">Rua Oitenta e sete, 418. CEP 41270-000 | Bairro Jardim Dois Irmaos - RS &nbsp;·&nbsp; www.valdonorte.example</p>
  </section>

  <!-- Envelope -->
  <section class="piece envelope" aria-label="Envelope">
    <div class="brand">
      <span class="brand-dot"></span>
      <span class="brand-name">ValdoNorte Residence<br>&amp; Geriatric SPA</span>
    </div>
    <p class="envelope-address">
      Rua Oitenta e sete, 418. CEP 41270-000<br>
      Bairro Jardim Dois Irmaos - RS
    </p>
    <svg class="wave" viewBox="0 0 620 120" preserveAspectRatio="none" aria-hidden="true">
      <defs>
        <linearGradient id="goldEnvelope" x1="0" y1="0" x2="1" y2="1">
          <stop offset="0" stop-color="#f0c463"/>
          <stop offset=".5" stop-color="#c98a1e"/>
          <stop offset="1" stop-color="#7a4a12"/>
        </linearGradient>
      </defs>
      <path d="M0 58 C200 120 420 20 620 44" fill="none" stroke="#6a8f2a" stroke-width="2"/>
      <path d="M0 70 C200 132 420 32 620 56 L620 120 L0 120 Z" fill="url(#goldEnvelope)"/>
    </svg>
    <p class="envelope-web">www.valdonorte.example</p>
  </section>

  <!-- Business card front -->
  <section class="piece card card-front" aria-label="Cartão de visita, frente">
    <div class="brand">
      <span class="brand-dot"></span>
      <span class="brand-name">ValdoNorte Residence<br>&amp; Geriatric SPA</span>
    </div>
    <svg class="wave" viewBox="0 0 300 80" preserveAspectRatio="none" aria-hidden="true">
      <defs>
        <linearGradient id="goldCard" x1="0" y1="0" x2="1" y2="1">
          <stop offset="0" stop-color="#f0c463"/>
          <stop offset=".5" stop-color="#c98a1e"/>
          <stop offset="1" stop-color="#7a4a12"/>
        </linearGradient>
      </defs>
      <path d="M0 22 C100 70 200 4 300 20" fill="none" stroke="#6a8f2a" stroke-width="1.5"/>
      <path d="M0 30 C100 78 200 12 300 28 L300 80 L0 80 Z" fill="url(#goldCard)"/>
    </svg>
    <p class="card-web">www.valdonorte.example</p>
  </section>

  <!-- Business card back -->
  <section class="piece card card-back" aria-label="Cartão de visita, verso">
    <svg class="wave" viewBox="0 0 300 70" preserveAspectRatio="none" aria-hidden="true">
      <path d="M0 0 L300 0 L300 10 C200 30 100 -10 0 52 Z" fill="#ffffff"/>
      <path d="M0 58 C100 -4 200 36 300 16" fill="none" stroke="#6a8f2a" stroke-width="1.5"/>
    </svg>
    <div class="contact">
      <p class="contact-name">Dra. Tereza Lopes Amaral</p>
      <p class="contact-role">Diretora</p>
      <p>Fone: (51) 3500-0000</p>
      <p>tereza@valdonorte.example</p>
      <p>Rua Oitenta e sete, 418. CEP 41270-000</p>
      <p>Bairro Jardim · Dois Irmaos - RS</p>
      <p>www.valdonorte.example</p>
    </div>
  </section>

</main>
</body>
</html>
```